Sunny Paths and joy Business card

I have a logo, but will like a business card design. Is for a travel agency in Mexico. We focus in family experiences.

I will liek some thing different and unique, from the traditional business card, something to get remmeber for.

Business card information:

Leandro T. Ocampo
leandro@sunnypathsjoy.example

Alameda 482, 3 piso
Col. Tlalpizco
Mexico, D.F. 07320

office: (55) 5000-0142
mobile: (55) 9000-0187

www.sunnypathsjoy.example
@sunnypjoy
blog: sunnypathsandjoy.blogsite.example
facebook: SunnyPathsAndJoy

```html
<!DOCTYPE html>
<html lang="en">
<head>
<meta charset="utf-8">
<title>Sunny Paths and joy – Business card</title>
<link rel="stylesheet" href="https://fonts.googleapis.com/css2?family=Quicksand:wght@500;700&display=swap">
<style>
  :root {
    --backdrop: #ece7e0;
    --card-white: #ffffff;
    --card-sky: #cfe6f7;
    --ink-blue: #4a9fcf;
    --ink-deep: #1f5f9e;
    --logo-blue: #2f66b3;
    --logo-halo: #cfe3f2;
    --splash: #c8def2;
  }
  * { box-sizing: border-box; margin: 0; padding: 0; }
  html, body { width: 1200px; height: 802px; overflow: hidden; }
  body {
    background: var(--backdrop);
    font-family: "Quicksand", sans-serif;
    display: flex;
    justify-content: center;
    align-items: center;
    gap: 70px;
  }
  .card {
    position: relative;
    width: 420px;
    height: 610px;
    border-radius: 34px;
    background: linear-gradient(to bottom, var(--card-white) 0%, var(--card-white) 45%, var(--card-sky) 100%);
    box-shadow: 0 6px 22px rgba(0,0,0,0.18);
    overflow: hidden;
    color: var(--ink-blue);
    letter-spacing: 0.18em;
    font-weight: 500;
  }
  /* Front */
  .brand {
    position: absolute;
    top: 40px;
    left: 30px;
    width: 300px;
  }
  .brand-artwork { display: block; width: 230px; height: 150px; margin-left: 30px; }
  .brand-name {
    margin-top: 6px;
    font-size: 40px;
    line-height: 1.05;
    font-weight: 700;
    letter-spacing: 0.02em;
    color: var(--logo-blue);
    text-align: center;
  }
  .front-details {
    position: absolute;
    left: 0; right: 0;
    bottom: 70px;
    text-align: center;
    font-size: 16px;
  }
  .holder-name { margin-bottom: 58px; }
  .front-details .line + .line { margin-top: 14px; }
  /* Back */
  .splash { position: absolute; top: 60px; left: 110px; width: 280px; height: 230px; }
  .back-details {
    position: absolute;
    left: 0; right: 0;
    top: 340px;
    text-align: center;
    font-size: 16px;
    line-height: 1.45;
  }
  .phones { margin-top: 22px; }
  .social {
    margin-top: 30px;
    font-size: 10px;
    line-height: 1.6;
    letter-spacing: 0.12em;
  }
</style>
</head>
<body>
  <article class="card card-front">
    <div class="brand">
      <svg class="brand-artwork" viewBox="0 0 230 150" role="img" aria-label="Logo illustration: cartoon blue airplane carrying two waving children">
        <ellipse cx="115" cy="80" rx="95" ry="62" fill="var(--logo-halo)"/>
        <ellipse cx="115" cy="80" rx="70" ry="34" fill="var(--logo-blue)" opacity="0.55"/>
      </svg>
      <p class="brand-name">Sunny Paths<br>and joy</p>
    </div>
    <div class="front-details">
      <p class="line holder-name">Leandro T. Ocampo</p>
      <p class="line">leandro@sunnypathsjoy.example</p>
      <p class="line">www.sunnypathsjoy.example</p>
    </div>
  </article>

  <article class="card card-back">
    <svg class="splash" viewBox="0 0 280 230" role="img" aria-label="Soft blue paint splash decoration">
      <path d="M60 40 C110 5 200 10 240 55 C280 100 265 180 215 205 C165 230 85 220 45 180 C5 140 15 75 60 40 Z" fill="var(--splash)"/>
    </svg>
    <div class="back-details">
      <p>Alameda 482, 3 piso</p>
      <p>Col. Tlalpizco</p>
      <p>Mexico, D.F. 07320</p>
      <div class="phones">
        <p>office: (55) 5000-0142</p>
        <p>mobile: (55) 9000-0187</p>
      </div>
      <div class="social">
        <p>@sunnypjoy</p>
        <p>blog: sunnypathsandjoy.blogsite.example</p>
        <p>facebook: SunnyPathsAndJoy</p>
      </div>
    </div>
  </article>
</body>
</html>
```